Sports Nutrition line needs new label look/feel

We need a new label design for "Velmo",our Sports Nutrition line of vitamins, nutraceuticals, protein powders, and performance endurance products. We would like to see two separate designs, one blue and one red, as these are the two colors we are torn between. The labels should have the look/feel of a sports or fitness label, bold coloring, lettering, and even some use of holographic foiling.
Brands we would be similar to those found on ploverstack.com and quillmarshgoods.com. Brands we like in particular are KTR and Temlux.

Target Market(s)

Fitness enthusiasts,athletes, health nuts..

Industry/Entity Type

Nutrition

Font styles to use
Sans Serif
Decorative
Script

Colors
ec1f27
0692cd
0355a3
3276b5
f04a50

Requirements
Must have
• -Fitness look/feel
• -bold colors (preferably red and blue)
• -use of icons (eye health, brain, health, etc.)
• -"Fit" in "VelMO" must stand out
• -use tagline "Fueling Stronger Lives"
Nice to have
• -holographic foiling elements
• -try to incorporate a molecular element (like those shown in the example labels)
Should not have
• -Light, calming colors
• -difficult to read fonts

```html
<!DOCTYPE html>
<html lang="en">
<head>
<meta charset="utf-8">
<title>Velmo Grape Seed Extract Labels</title>
<link rel="stylesheet" href="https://fonts.googleapis.com/css2?family=Oswald:wght@500;700&family=Roboto+Condensed:ital,wght@0,400;1,500&family=Roboto:wght@400&display=swap">
<style>
  :root {
    --page-bg: #eceeed;
    --silver-light: #e6e8ea;
    --silver-dark: #8a8e92;
    --white: #ffffff;
    --blue-deep: #0355a3;
    --blue-mid: #3276b5;
    --blue-bright: #0692cd;
    --blue-ink: #0a2f6b;
    --red-deep: #b3121a;
    --red-mid: #ec1f27;
    --red-bright: #f04a50;
    --red-ink: #5e0a0e;
  }
  * { box-sizing: border-box; margin: 0; padding: 0; }
  html, body { width: 1200px; height: 1200px; overflow: hidden; }
  body {
    background: linear-gradient(180deg, #f3f4f4 0%, var(--page-bg) 55%, #e4e7e7 100%);
    display: flex; align-items: center; justify-content: center; gap: 60px;
  }
  .icon-defs { position: absolute; width: 0; height: 0; }

  .label {
    position: relative;
    width: 520px; height: 580px;
    overflow: hidden;
    color: var(--white);
    box-shadow: 0 12px 30px rgba(0,0,0,.18);
  }
  .label--blue { --c-deep: var(--blue-deep); --c-mid: var(--blue-mid); --c-bright: var(--blue-bright); --c-ink: var(--blue-ink); }
  .label--red  { --c-deep: var(--red-deep);  --c-mid: var(--red-mid);  --c-bright: var(--red-bright);  --c-ink: var(--red-ink); }

  .label__field {
    position: absolute; inset: 0;
    background: linear-gradient(135deg, var(--c-bright) 0%, var(--c-mid) 40%, var(--c-deep) 100%);
  }
  .label__artwork {
    position: absolute; left: 0; top: 14px; width: 300px; height: 300px;
    background: radial-gradient(ellipse at 40% 45%, rgba(255,255,255,.16) 0%, rgba(0,0,0,.12) 60%, transparent 75%);
  }
  .label__band {
    position: absolute; left: 0; right: 0; height: 14px;
    background: linear-gradient(180deg, var(--silver-light), var(--silver-dark) 60%, var(--silver-light));
  }
  .label__band--top { top: 0; }
  .label__band--bottom { bottom: 0; }

  .brand {
    position: absolute; top: 110px; left: 0; right: 0;
    display: flex; flex-direction: column; align-items: center; padding-left: 120px;
  }
  .brand__row { display: flex; align-items: center; gap: 12px; }
  .brand__dot { width: 22px; height: 22px; border-radius: 50%; background: var(--white); }
  .brand__name {
    font-family: "Oswald", sans-serif; font-weight: 700;
    font-size: 80px; line-height: 1; letter-spacing: -1px; color: var(--white);
  }
  .brand__tagline {
    font-family: "Roboto", sans-serif; font-weight: 400;
    font-size: 21px; margin-top: 4px; color: var(--white);
  }

  .product {
    position: absolute; top: 250px; left: 0; right: 0; text-align: center;
  }
  .product__name {
    font-family: "Oswald", sans-serif; font-weight: 700;
    font-size: 66px; line-height: 1; letter-spacing: -1px;
    transform: scaleX(.92);
    text-shadow: 2px 2px 0 var(--c-ink), -1px -1px 0 var(--c-ink), 1px -1px 0 var(--c-ink), -1px 1px 0 var(--c-ink);
  }
  .product__claim {
    font-family: "Roboto Condensed", sans-serif; font-style: italic; font-weight: 500;
    font-size: 25px; margin-top: 14px;
  }

  .benefits {
    position: absolute; top: 392px; left: 22px; right: 22px;
    display: flex; justify-content: space-between; list-style: none;
  }
  .benefit {
    width: 76px; height: 76px; border-radius: 50%;
    background: var(--white); border: 4px solid var(--c-ink);
    display: flex; align-items: center; justify-content: center;
    color: var(--c-mid);
  }
  .benefit svg { width: 46px; height: 46px; }

  .supply {
    position: absolute; right: 40px; bottom: 58px; text-align: right;
    font-family: "Roboto Condensed", sans-serif; font-weight: 400;
    font-size: 20px; line-height: 1.25; transform: rotate(-4deg);
  }
</style>
</head>
<body>

<svg class="icon-defs" aria-hidden="true">
  <defs>
    <symbol id="icon-joint" viewBox="0 0 48 48">
      <rect x="10" y="4" width="12" height="20" rx="6" fill="currentColor" transform="rotate(-20 16 14)"/>
      <rect x="24" y="22" width="12" height="22" rx="6" fill="currentColor" transform="rotate(-20 30 33)"/>
      <circle cx="24" cy="24" r="6" fill="none" stroke="currentColor" stroke-width="3"/>
    </symbol>
    <symbol id="icon-brain" viewBox="0 0 48 48">
      <ellipse cx="24" cy="22" rx="19" ry="14" fill="currentColor"/>
      <path d="M24 9v26M12 17c4 2 6 6 4 10M36 17c-4 2-6 6-4 10" stroke="#fff" stroke-width="2" fill="none"/>
      <rect x="26" y="32" width="6" height="10" rx="2" fill="currentColor"/>
    </symbol>
    <symbol id="icon-hair" viewBox="0 0 48 48">
      <path d="M14 38c0-12 2-20 4-28M22 38c0-12 1-20 2-30M30 38c0-12-1-20-2-28M38 38c-1-10-3-18-6-24" stroke="currentColor" stroke-width="2.5" fill="none"/>
      <rect x="6" y="38" width="36" height="5" rx="2" fill="currentColor"/>
    </symbol>
    <symbol id="icon-eye" viewBox="0 0 48 48">
      <path d="M4 24C12 10 36 10 44 24 36 38 12 38 4 24Z" fill="none" stroke="currentColor" stroke-width="3"/>
      <ellipse cx="24" cy="24" rx="7" ry="10" fill="none" stroke="currentColor" stroke-width="3"/>
      <circle cx="24" cy="24" r="3" fill="currentColor"/>
    </symbol>
    <symbol id="icon-cells" viewBox="0 0 48 48">
      <ellipse cx="26" cy="16" rx="16" ry="8" fill="currentColor" transform="rotate(-15 26 16)"/>
      <ellipse cx="22" cy="32" rx="16" ry="8" fill="currentColor" transform="rotate(-15 22 32)"/>
      <ellipse cx="26" cy="16" rx="7" ry="3" fill="#fff" transform="rotate(-15 26 16)"/>
      <ellipse cx="22" cy="32" rx="7" ry="3" fill="#fff" transform="rotate(-15 22 32)"/>
    </symbol>
  </defs>
</svg>

<article class="label label--blue">
  <div class="label__field"></div>
  <div class="label__artwork" role="img" aria-label="Flexing athlete silhouette over a molecular network pattern"></div>
  <div class="label__band label__band--top"></div>
  <div class="brand">
    <div class="brand__row"><span class="brand__dot"></span><span class="brand__name">Velmo</span></div>
    <p class="brand__tagline">Fueling Stronger Lives</p>
  </div>
  <div class="product">
    <h1 class="product__name">Grape Seed Extract</h1>
    <p class="product__claim">Antioxidant Formula to Boost Immunity</p>
  </div>
  <ul class="benefits">
    <li class="benefit"><svg><use href="#icon-joint"/></svg></li>
    <li class="benefit"><svg><use href="#icon-brain"/></svg></li>
    <li class="benefit"><svg><use href="#icon-hair"/></svg></li>
    <li class="benefit"><svg><use href="#icon-eye"/></svg></li>
    <li class="benefit"><svg><use href="#icon-cells"/></svg></li>
  </ul>
  <p class="supply">90 Day Supply<br>Dietary Supplement</p>
  <div class="label__band label__band--bottom"></div>
</article>

<article class="label label--red">
  <div class="label__field"></div>
  <div class="label__artwork" role="img" aria-label="Flexing athlete silhouette over a molecular network pattern"></div>
  <div class="label__band label__band--top"></div>
  <div class="brand">
    <div class="brand__row"><span class="brand__dot"></span><span class="brand__name">Velmo</span></div>
    <p class="brand__tagline">Fueling Stronger Lives</p>
  </div>
  <div class="product">
    <h1 class="product__name">Grape Seed Extract</h1>
    <p class="product__claim">Antioxidant Formula to Boost Immunity</p>
  </div>
  <ul class="benefits">
    <li class="benefit"><svg><use href="#icon-joint"/></svg></li>
    <li class="benefit"><svg><use href="#icon-brain"/></svg></li>
    <li class="benefit"><svg><use href="#icon-hair"/></svg></li>
    <li class="benefit"><svg><use href="#icon-eye"/></svg></li>
    <li class="benefit"><svg><use href="#icon-cells"/></svg></li>
  </ul>
  <p class="supply">90 Day Supply<br>Dietary Supplement</p>
  <div class="label__band label__band--bottom"></div>
</article>

</body>
</html>
```